Simple landing page for Tumbles cookbook

I need a one page landingpage where customers can order the cookbook.
This is a cookbook of a collection of recipes from our deli that we used to run.
I need a landing page where customers can come and order the book. I also need it coded. I already have the domain through hostvarn.
I can send the file of the book through sendlumo. It's too big to upload here. Just so you get the feel that I am looking for.
I attached a simple text as an introduction to the page. But I am open to any suggestions. I want it all to be about the experience that we are sharing the recipes with everybody and that it's for sale. The book is $29.99, shipping included.
Customers have to be able to click and buy the book from it.

Coding

Coded - Design and coding required

Number of Pages Required

1 page

Font styles to use
Sans Serif

Requirements
Must have
• Same colors as the cookbook

```html
<!DOCTYPE html>
<html lang="en">
<head>
<meta charset="utf-8">
<title>Tumbles Sandwiches – Favorite Recipes In One Book</title>
<link href="https://fonts.googleapis.com/css2?family=Oswald:wght@500;600&family=Quicksand:wght@500;600&display=swap" rel="stylesheet">
<style>
:root{
  --brown:#3a2213;
  --crimson:#c21d5a;
  --blue:#2f86b8;
  --blue-deep:#1d5478;
  --sky:#cfe3f2;
  --sky-soft:#e8f2f9;
  --olive:#8d9a3c;
  --ink:#1d1d1d;
  --white:#ffffff;
}
*{margin:0;padding:0;box-sizing:border-box}
html,body{width:1200px;height:3156px;overflow:hidden;background:var(--white)}
body{position:relative;font-family:"Quicksand",sans-serif;color:var(--ink)}
.abs{position:absolute}
.heading{font-family:"Oswald",sans-serif;font-weight:600;letter-spacing:2px;text-transform:uppercase;color:var(--brown)}
.btn{position:absolute;display:flex;align-items:center;justify-content:center;background:var(--crimson);color:var(--white);
  font-family:"Oswald",sans-serif;font-weight:500;font-size:16px;letter-spacing:2px;border-radius:20px;text-decoration:none;
  box-shadow:0 4px 10px rgba(194,29,90,.3)}
.brand{font-family:"Oswald",sans-serif;font-weight:600;color:var(--brown);line-height:1;letter-spacing:1px}
.brand small{display:block;font-size:.45em;letter-spacing:1px;margin-top:2px}

/* hero */
.hero{left:0;top:0;width:1200px;height:612px;overflow:hidden;background:linear-gradient(180deg,#fff 0%,#f4f8fb 100%)}
.hero-band{left:0;top:612px;width:1200px;height:8px;background:#6ea6cf}
.hero-logo{left:147px;top:42px;font-size:40px}
.hero-title{left:145px;top:208px;font-size:48px;line-height:52px;letter-spacing:4px}
.hero-sub{left:145px;top:325px;width:420px;font-size:13.5px;line-height:19px;letter-spacing:.8px;font-weight:600}
.includes{left:145px;top:392px;font-size:18px;letter-spacing:1.5px;font-weight:600;text-transform:uppercase;color:var(--brown)}
.includes em{font-style:normal;color:var(--crimson);font-size:22px}
.include-list{left:145px;top:430px;display:flex;gap:30px;font-size:13.5px;font-weight:600;letter-spacing:1px}
.include-list span{display:flex;align-items:center;gap:8px}
.book-hero{left:682px;top:72px;width:340px;height:500px;border-radius:6px 14px 14px 6px;
  background:linear-gradient(160deg,#e9f2f8 0%,#d6e6f1 45%,#c9a56f 60%,#e8eef3 85%);box-shadow:14px 14px 30px rgba(40,70,100,.3)}

.badge{width:110px;height:110px;border-radius:50%;background:radial-gradient(circle,#d42a68 0%,#b8164f 70%);
  box-shadow:0 0 30px rgba(194,29,90,.45);color:var(--white);display:flex;flex-direction:column;align-items:center;justify-content:center}
.badge .price{font-family:"Oswald",sans-serif;font-weight:600;font-size:28px;line-height:1;letter-spacing:1px}
.badge .price sup{font-size:13px;vertical-align:top}
.badge .ship{display:flex;align-items:center;gap:4px;font-size:8px;line-height:9px;margin-top:3px}

/* partners */
.partners-tab{left:471px;top:612px;width:260px;height:50px;background:#6ea6cf;border-radius:0 0 40px 40px;
  color:var(--white);font-family:"Oswald",sans-serif;font-weight:500;font-size:22px;letter-spacing:3px;
  display:flex;align-items:center;justify-content:center;box-shadow:0 4px 8px rgba(0,0,0,.15)}
.partner{top:700px;height:32px;background:#8c8c8c;border-radius:16px;opacity:.85}

/* feature card */
.feature-photo{left:145px;top:780px;width:459px;height:681px;border-radius:8px 0 0 8px;
  background:linear-gradient(160deg,#6f8f45 0%,#d9b26a 40%,#e8cf8e 60%,#3a2a1c 100%)}
.feature-panel{left:604px;top:780px;width:451px;height:648px;border-radius:0 8px 8px 0;
  background:linear-gradient(180deg,var(--blue) 0%,var(--blue-deep) 100%);color:var(--white)}
.feature-item{position:absolute;left:33px;width:390px}
.feature-item h3{font-family:"Oswald",sans-serif;font-weight:500;font-size:23px;letter-spacing:2px;text-transform:uppercase;margin-bottom:14px}
.feature-item p{font-size:13px;line-height:19px;letter-spacing:.8px;font-weight:600}
.quote-box{left:279px;top:1371px;width:642px;height:134px;background:var(--white);border-radius:12px;
  box-shadow:0 10px 24px rgba(0,0,0,.18);display:flex;align-items:center;justify-content:center;text-align:center;
  font-size:17px;line-height:29px;letter-spacing:1.5px;font-weight:600;padding-top:10px}
.quote-mark{width:62px;height:62px;border-radius:50%;background:var(--crimson);box-shadow:0 0 18px rgba(194,29,90,.4);
  display:flex;align-items:center;justify-content:center}

/* story */
.story-photo{left:588px;top:1580px;width:612px;height:526px;
  background:radial-gradient(ellipse at 60% 45%,#8a5a34 0%,#c99a62 30%,#e2c8a8 50%,rgba(255,255,255,0) 72%)}
.story-item{position:absolute;left:159px;width:410px}
.story-item .label{color:var(--olive);font-size:13px;letter-spacing:1px;font-weight:600;margin-bottom:6px}
.story-item h3{font-size:23px;letter-spacing:2.5px;margin-bottom:10px}
.story-item p{font-size:13px;line-height:19px;letter-spacing:.8px;font-weight:600}

/* offer */
.offer-books{left:0;top:2082px;width:667px;height:428px;
  background:linear-gradient(150deg,rgba(220,232,242,0) 0%,#c8d9e6 30%,#c9a570 55%,#b8cad8 80%,rgba(220,232,242,0) 100%);
  clip-path:polygon(0 30%,45% 0,100% 48%,60% 100%,0 78%)}
.offer-title{left:600px;top:2206px;width:494px;text-align:center;font-size:48px;line-height:52px;letter-spacing:4px}
.offer-sub{left:660px;top:2324px;width:374px;text-align:center;font-size:13.5px;line-height:19px;letter-spacing:.8px;font-weight:600}

/* closing */
.foot-logo{left:0;top:2550px;width:1200px;text-align:center;font-size:30px}
.closing-title{left:0;top:2626px;width:1200px;text-align:center;font-size:23px;line-height:32px;letter-spacing:2.5px}
.closing-panel{left:145px;top:2740px;width:910px;height:416px;border-radius:10px 10px 0 0;
  background:linear-gradient(180deg,var(--blue) 0%,var(--blue-deep) 60%,#153c57 100%)}
.closing-text{left:260px;top:2794px;width:680px;text-align:center;color:var(--white);font-size:17px;line-height:29px;letter-spacing:1.5px;font-weight:600}
.closing-food{left:49px;top:2925px;width:1096px;height:231px;
  background:linear-gradient(180deg,#d9a85a 0%,#4f7a2c 35%,#2f5a1d 70%,#1d3a12 100%);
  clip-path:polygon(5% 40%,12% 12%,40% 4%,70% 6%,93% 0,96% 30%,100% 100%,0 100%)}
.copyright{left:0;top:3114px;width:1200px;text-align:center;color:var(--white);font-size:14px;font-weight:500}
.copyright u{text-underline-offset:2px}
</style>
</head>
<body>

<!-- hero -->
<section class="abs hero">
  <svg class="abs" style="left:0;top:0" width="1200" height="612" viewBox="0 0 1200 612">
    <path d="M0 235 C220 140 430 110 700 170 L700 612 L0 612Z" fill="#d3e5f2"/>
    <path d="M0 400 C180 280 380 220 620 260 C700 280 760 330 820 380 L820 612 L0 612Z" fill="#c2dbee" opacity=".7"/>
    <path d="M120 150 C320 90 520 70 700 120" stroke="#fff" stroke-width="18" fill="none" opacity=".8"/>
    <path d="M700 0 L1200 0 L1200 612 L620 612 C760 520 840 400 860 260 C880 140 820 60 700 0Z" fill="#dbe9f4" opacity=".6"/>
  </svg>
  <div class="abs brand hero-logo">TUMBLES<small>SANDWICHES</small></div>
  <h1 class="abs heading hero-title">Favorite Recipes<br>In One Book</h1>
  <p class="abs hero-sub">Surprise Family And Friends With Branded Sandwiches From Tumbles</p>
  <p class="abs includes">Book includes <em>28 recipes</em>:</p>
  <div class="abs include-list">
    <span><svg width="20" height="14" viewBox="0 0 20 14"><path d="M2 6 Q10 0 18 6Z M2 8 H18 M2 11 H18" stroke="#777" stroke-width="1.4" fill="none"/></svg>Sandwiches</span>
    <span><svg width="20" height="14" viewBox="0 0 20 14"><path d="M1 4 H19 L15 12 H5Z M8 4 V1 H12" stroke="#777" stroke-width="1.4" fill="none"/></svg>Sauces</span>
    <span><svg width="20" height="16" viewBox="0 0 20 16"><path d="M2 7 Q10 -1 18 7Z M2 10 H18 M3 13 H17" stroke="#777" stroke-width="1.4" fill="none"/></svg>Burgers</span>
  </div>
  <a class="btn" href="#order" style="left:145px;top:476px;width:152px;height:36px">BYU NOW</a>
  <div class="abs book-hero" role="img" aria-label="Cookbook cover with a sandwich photo, titled Your ultimate guide to creating your own favourite Tumbles sandwiches, 28 delicious recipes"></div>
  <div class="abs badge" style="left:588px;top:214px">
    <div class="price"><sup>$</sup>29.99</div>
    <div class="ship"><svg width="18" height="11" viewBox="0 0 18 11"><path d="M1 1 H11 V8 H1Z M11 4 H15 L17 7 V8 H11" stroke="#fff" stroke-width="1.2" fill="none"/><circle cx="4" cy="9" r="1.5" fill="#fff"/><circle cx="14" cy="9" r="1.5" fill="#fff"/></svg>Free<br>Shipping</div>
  </div>
</section>
<div class="abs hero-band"></div>

<!-- partners -->
<div class="abs partners-tab">PARTNERS</div>
<div class="abs partner" style="left:239px;width:154px" aria-label="Partner badge"></div>
<div class="abs partner" style="left:466px;width:118px" aria-label="Partner badge"></div>
<div class="abs partner" style="left:651px;width:130px" aria-label="Partner badge"></div>
<div class="abs partner" style="left:848px;width:124px" aria-label="Partner badge"></div>

<!-- feature card -->
<div class="abs feature-photo" role="img" aria-label="Hand pulling apart a toasted cheese panini"></div>
<section class="abs feature-panel">
  <div class="feature-item" style="top:76px"><h3>Favorite Recipes In One Book</h3><p>Lorem ipsum dolor sit amet, consectetur adipiscing elit. Magna pulvinar vestibulum bibendum dictum dignissim dictum auctor fusce eget.</p></div>
  <div class="feature-item" style="top:204px"><h3>Favorite Recipes In One Book</h3><p>Quis blandit sem viverra aliquam posuere risus semper eu. Faucibus mattis ipsum imperdiet molestie.</p></div>
  <div class="feature-item" style="top:334px"><h3>Favorite Recipes In One Book</h3><p>Dignissim ipsum vivamus sed habitant sed tincidunt nibh sed a. Tellus consequat adipiscing elit nisi. Eget in ullamcorper id pharetra, nisl.</p></div>
  <a class="btn" href="#order" style="left:33px;top:464px;width:152px;height:37px">BYU NOW</a>
</section>
<div class="abs quote-box">We Truly Hope You Will Enjoy Making These Sandwiches<br>Just As Much As We Did.</div>
<div class="abs quote-mark" style="left:568px;top:1339px"><svg width="32" height="22" viewBox="0 0 32 22"><path d="M8 2 a6 6 0 1 0 6 6 V10 Q14 17 6 20 M24 2 a6 6 0 1 0 6 6 V10 Q30 17 22 20" stroke="#fff" stroke-width="2.6" fill="none" stroke-linecap="round"/></svg></div>

<!-- story + offer background wave -->
<svg class="abs" style="left:0;top:1860px" width="1200" height="660" viewBox="0 0 1200 660">
  <path d="M0 30 C200 160 480 250 760 250 C950 250 1100 200 1200 150 L1200 640 L0 640Z" fill="#d6e7f3"/>
  <path d="M0 120 C260 300 560 300 820 270 C1000 250 1120 210 1200 190 L1200 640 L0 640Z" fill="#c7ddef"/>
  <path d="M300 440 C600 360 900 380 1200 300" stroke="#fff" stroke-width="10" fill="none" opacity=".7"/>
</svg>

<div class="abs story-photo" role="img" aria-label="Hand holding a bitten beef burger"></div>
<div class="story-item" style="top:1674px"><p class="label">Lorem ipsum dolor</p><h3 class="heading">Favorite Recipes In One Book</h3><p>Lorem ipsum dolor sit amet, consectetur adipiscing elit. Magna pulvinar vestibulum bibendum dictum dignissim dictum auctor fusce eget.</p></div>
<div class="story-item" style="top:1837px"><p class="label">Lorem ipsum dolor</p><h3 class="heading">Favorite Recipes In One Book</h3><p>Quis blandit sem viverra aliquam posuere risus semper eu. Faucibus mattis ipsum imperdiet molestie.</p></div>

<div class="abs offer-books" role="img" aria-label="Two copies of the Tumbles sandwich cookbook lying at an angle"></div>
<div class="abs badge" style="left:792px;top:2082px">
  <div class="price"><sup>$</sup>29.99</div>
  <div class="ship"><svg width="18" height="11" viewBox="0 0 18 11"><path d="M1 1 H11 V8 H1Z M11 4 H15 L17 7 V8 H11" stroke="#fff" stroke-width="1.2" fill="none"/><circle cx="4" cy="9" r="1.5" fill="#fff"/><circle cx="14" cy="9" r="1.5" fill="#fff"/></svg>Free<br>Shipping</div>
</div>
<h2 class="abs heading offer-title">Favorite Recipes<br>In One Book</h2>
<p class="abs offer-sub">Surprise Family And Friends With Branded Sandwiches From Tumbles</p>
<a class="btn" id="order" href="#order" style="left:771px;top:2380px;width:153px;height:37px">BYU NOW</a>

<!-- closing -->
<div class="abs brand foot-logo">TUMBLES<small>SANDWICHES</small></div>
<h2 class="abs heading closing-title">Quis blandit sem viverra aliquam posuere<br>risus semper eu.</h2>
<div class="abs closing-panel"></div>
<div class="abs quote-mark" style="left:568px;top:2708px"><svg width="32" height="22" viewBox="0 0 32 22"><path d="M8 2 a6 6 0 1 0 6 6 V10 Q14 17 6 20 M24 2 a6 6 0 1 0 6 6 V10 Q30 17 22 20" stroke="#fff" stroke-width="2.6" fill="none" stroke-linecap="round"/></svg></div>
<p class="abs closing-text">Unfortunately, we can't open another Tumbles, but we can offer you this collection of our recipes for you to try out at home with your family and friends.</p>
<div class="abs closing-food" role="img" aria-label="Close-up of a toasted sandwich loaded with fresh spinach leaves"></div>
<p class="abs copyright">Copyright 2022. <u>Tumbles Sandwiches</u> | All Rights Reserved</p>

</body>
</html>
```